Hall of Fame announcement social media post

I need a social media Hall of Fame announcement designed in the styles of some of the examples I've posted. I have attached the two gentlemens head shots ... the names are Carl Whitby and Ron Fadley

It is for the TENNESSEE LINKS LEGENDS GALLERY also include 2025 Inductees ... I have also attached the logo... make the post in similar colors as the logo

```html
<!DOCTYPE html>
<html lang="en">
<head>
<meta charset="utf-8">
<title>2025 Inductees – Tennessee Links Legends Gallery</title>
<link href="https://fonts.googleapis.com/css2?family=Josefin+Sans:wght@700&family=Libre+Baskerville:wght@700&display=swap" rel="stylesheet">
<style>
  :root {
    --navy: #0f1f4f;
    --navy-deep: #071640;
    --red: #b8261f;
    --red-soft: #d0605a;
    --white: #ffffff;
  }
  * { margin: 0; padding: 0; box-sizing: border-box; }
  html, body { width: 1200px; height: 675px; overflow: hidden; background: var(--white); }
  .post {
    position: relative;
    width: 1200px;
    height: 675px;
    overflow: hidden;
    background: var(--white);
    font-family: "Josefin Sans", sans-serif;
  }
  .backdrop-photo {
    position: absolute;
    left: 110px; top: 0;
    width: 460px; height: 600px;
    background: radial-gradient(ellipse at 50% 45%, rgba(190,190,190,0.45), rgba(235,235,235,0.2) 60%, rgba(255,255,255,0) 80%);
  }
  .stripes { position: absolute; inset: 0; width: 1200px; height: 675px; z-index: 1; }
  .headline {
    position: absolute;
    left: 120px; top: 98px;
    width: 330px;
    text-align: center;
    color: var(--navy);
    font-weight: 700;
    font-size: 98px;
    line-height: 94px;
    letter-spacing: 4px;
    z-index: 2;
  }
  .headline span { display: block; }
  .subhead {
    position: absolute;
    left: 120px; top: 400px;
    width: 330px;
    text-align: center;
    color: var(--red);
    font-weight: 700;
    font-size: 32px;
    letter-spacing: 1.5px;
    z-index: 2;
  }
  .brand-name {
    position: absolute;
    left: 180px; top: 490px;
    width: 200px;
    text-align: center;
    color: var(--navy);
    font-family: "Libre Baskerville", serif;
    font-weight: 700;
    font-size: 19px;
    line-height: 24px;
    z-index: 2;
  }
  .inductee {
    position: absolute;
    width: 240px;
    text-align: center;
    color: var(--white);
    z-index: 3;
  }
  .inductee--first { left: 542px; top: 466px; }
  .inductee--second { left: 836px; top: 466px; }
  .inductee__name {
    font-weight: 700;
    font-size: 22px;
    letter-spacing: 1.5px;
    text-transform: uppercase;
    white-space: nowrap;
  }
  .inductee__stars { display: block; margin: 10px auto 0; }
</style>
</head>
<body>
<main class="post">
  <div class="backdrop-photo" role="img" aria-label="Faded black-and-white photo of a golfer finishing a swing"></div>

  <svg class="stripes" viewBox="0 0 1920 1080" aria-hidden="true">
    <defs>
      <linearGradient id="redFade" x1="0" y1="1" x2="0.6" y2="0">
        <stop offset="0" stop-color="#d0605a"/>
        <stop offset="1" stop-color="#b8261f"/>
      </linearGradient>
      <linearGradient id="navyFade" x1="0" y1="1" x2="0.5" y2="0">
        <stop offset="0" stop-color="#2a3d6e"/>
        <stop offset="0.4" stop-color="#071640"/>
        <stop offset="1" stop-color="#071640"/>
      </linearGradient>
      <linearGradient id="portraitOne" x1="0" y1="0" x2="0" y2="1">
        <stop offset="0" stop-color="#dfe3ea"/>
        <stop offset="0.5" stop-color="#c99a80"/>
        <stop offset="1" stop-color="#2b2b33"/>
      </linearGradient>
      <linearGradient id="portraitTwo" x1="0" y1="0" x2="0" y2="1">
        <stop offset="0" stop-color="#2f6fd0"/>
        <stop offset="0.55" stop-color="#c98f7f"/>
        <stop offset="1" stop-color="#1f2430"/>
      </linearGradient>
    </defs>
    <polygon class="band band--red" points="1090,0 1338,0 948,855 700,855" fill="url(#redFade)"/>
    <polygon class="band band--navy" points="1338,0 1895,0 1745,365 1800,510 1480,1080 845,1080" fill="url(#navyFade)"/>
    <polygon class="band band--red-low" points="1770,510 1920,510 1920,540 1715,1080 1465,1080" fill="#b8261f"/>

    <circle cx="1067" cy="477" r="240" fill="#ffffff"/>
    <circle cx="1067" cy="477" r="220" fill="url(#portraitOne)" role="img" aria-label="Headshot of Carl Whitby"/>
    <circle cx="1530" cy="485" r="240" fill="#ffffff"/>
    <circle cx="1530" cy="485" r="220" fill="url(#portraitTwo)" role="img" aria-label="Headshot of Ron Fadley"/>
  </svg>

  <h1 class="headline"><span>HALL</span><span>OF</span><span>FAME</span></h1>
  <p class="subhead">2025 INDUCTEES</p>

  <p class="brand-name">TENNESSEE LINKS LEGENDS GALLERY</p>

  <div class="inductee inductee--first">
    <p class="inductee__name">Carl Whitby</p>
    <svg class="inductee__stars" width="80" height="22" viewBox="0 0 80 22" aria-hidden="true">
      <g fill="#ffffff">
        <polygon points="11,0 13.6,7.6 21.5,7.6 15.2,12.4 17.5,20 11,15.4 4.5,20 6.8,12.4 0.5,7.6 8.4,7.6"/>
        <polygon transform="translate(29 0)" points="11,0 13.6,7.6 21.5,7.6 15.2,12.4 17.5,20 11,15.4 4.5,20 6.8,12.4 0.5,7.6 8.4,7.6"/>
        <polygon transform="translate(58 0)" points="11,0 13.6,7.6 21.5,7.6 15.2,12.4 17.5,20 11,15.4 4.5,20 6.8,12.4 0.5,7.6 8.4,7.6"/>
      </g>
    </svg>
  </div>

  <div class="inductee inductee--second">
    <p class="inductee__name">Ron Fadley</p>
    <svg class="inductee__stars" width="80" height="22" viewBox="0 0 80 22" aria-hidden="true">
      <g fill="#ffffff">
        <polygon points="11,0 13.6,7.6 21.5,7.6 15.2,12.4 17.5,20 11,15.4 4.5,20 6.8,12.4 0.5,7.6 8.4,7.6"/>
        <polygon transform="translate(29 0)" points="11,0 13.6,7.6 21.5,7.6 15.2,12.4 17.5,20 11,15.4 4.5,20 6.8,12.4 0.5,7.6 8.4,7.6"/>
        <polygon transform="translate(58 0)" points="11,0 13.6,7.6 21.5,7.6 15.2,12.4 17.5,20 11,15.4 4.5,20 6.8,12.4 0.5,7.6 8.4,7.6"/>
      </g>
    </svg>
  </div>
</main>
</body>
</html>
```